Tolliver for Governor
We have chosen draft #108.
You have all done a great job and are amazing designers. I hope to work with you all again on future design projects for Tolliver For Governor.
Envelope: Move the address and URL up to just below the gold swoosh and you're missing a 't' in www.TolliverForGovernor.example On the back make the whole back white again add back in the emblem on the flap and make the It's Our Time fit across the back of the envelope in blue with a gradient.
Cards: Please see image and message.
Letterhead: Spot on!!!
We are now looking at #102, #103 and #106. Thank you to all the other designers, you've done a great job. There is still time for everyone to revise and resubmit their drafts, based on the comments we've made.
#90, Remove the email address from the letterhead and add Paid For By Tolliver For Governor on the same line as tolliverforgovernor.example, but on the far left side of page. Add address next to logo on front of envelope and lower It's Our Time on the back of the envelope. Remove the vertical It's Our Time from the two blue cards and center the logo on the blue card that should have no text.
#87, I like it. But everywhere you have tolliverforgovernor.example (except email addresses) remove it. I don't actually want the ""s around It's Our Time. It was away of telling you all what the exact text was. On the left side, the bottom two cards you could replace the URL with It's Our Time, just make the text bigger and bolder.
Envelope: I would like to see the back panel (not the flap) blue with white text saying "It's Our Time". On the front, move the address to the right side of the logo just under the gold swish. Add the URL under the address. Also, the address should be on 2 lines
P.O. Box 71832
Indianapolis, IN 46917
www.TolliverForGovernor.example
Card:
Logo-side, make the text much bigger (across the card bottom) and diffuse and spread out the white halo.
Info-side, move the phone number to it's own line above the address and move Name and title lines up to the lowest point in the gold swoosh. Try making the "tolliverforgovernor" in www.tolliverforgovernor.example blue like Jorel Drennick and capitalize the R,F and G.
Letterhead: on the same line as the phone and URL, but on the left side of the page, need "Paid For By Tolliver For Governor". Move the watermark logo up the page a little bit and add the line "It's Our Time" as light gray-ish watermark under it.
I done, please check
#80, please remove the URL from the logo-sides and insert the address on the info-side
please check private message
#45 and #43, let's lighten the background on the logo-side, remove the URL from both sides and insert the address.
#46, can we make the logo on the left side bigger, raise the name/title up more, insert the address and make the text bolder. On the logo side, lighter and more diffused. Also, please upload drafts for a letterhead and envelope.
I meant the logo-sides from #72 and #74
ALL: please include "Paid For By Tolliver For Governor" in small font at the bottom of the letterhead.
#70, this may be confusing, bare with me.
I like the info-side from #70 but; with the address added, name/title moved up and name in blue and remove the "phone" & "email" tags.
I like the logo-side but; make the white border around the logo the same size as the info-side and replace the URL with "It's Our Time" in font/style like "for Governor".
Would you be willing to add in the logo-side cards from both #71 and #74? Could you make the white border around the logos like the ones on the info-side in #70?
Also, need your drafts for an envelope and letterhead.
#13, I like the gradient on the front. Let's lighten the gradient, make the logo bigger and add some white diffusion around the logo (subtle). On the info side - like the flame in the lower corner. Raise the name and title area, make the name a little darker, remove the URL from the blue band, remove the "phone" and "email" tags, insert the full address. Maybe fill the center with a watermark of the logo? Also, would like to see some drafts for the letterhead and envelope.
Cards:
Info side- move name and title up more, put in the full address and add "It's Our Time" across the bottom in the same font style as "Tolliver".
Logo side- keep the logo transparency in the center of the logo, make the logo bigger and replace the white background with a light blue gradient (like in the images we uploaded).
Letterhead: remove all contact info except address, phone and URL. Add a "watermark" of all or part of the logo (w/ out the "Tolliver"). Also, at the bottom in the same line as the URL, but on the left side, add "Paid For By Tolliver For Governor".
Envelope: Insert the full address, move address and URL to the right of the logo (just under the gold line) on the back (not the flap) add "It's Our Time" feel free to try different colors in that area.
ALL: the card does not need to say "phone" or "email". You can use an icon if you want, but no need to spell it out. Also, only have the address, phone and URL on the letterhead.
Vandrel (#65,#64,#63,#62,#61,#60), What happened to the logo? Why is there sections (like a bar going across it) missing?
Sorry everyone, We've been on the road and unable to post more information or critiques.
Project Details:
1. This is a full stationary project (2-side business card, letterhead and envelope).
2. Front of business card should have either "It's Our Time" and the emblem from our provided logo or just the emblem. Background should be a light blue radial gradient with very light whitening behind emblem and/or text. Font for "It's Our Time" should match the fonts used for "Tolliver" in provided logo (colors either the same or white).
3. Address is:
PO Box 71832
4. Letterhead should have a watermark using all or part of the emblem from the provided logo.
5. Envelope should have a return address (PO Box from above).
6. Our campaign slogan is "It's Our Time".
7. On the business card there needs to be an area between the name/title area and the contact info.
8. Please do not fill in the transparent parts of the emblem or change it's color.
We will be picking a winner in the next 24 hours or less.
Good luck everyone :)

```html
<!DOCTYPE html>
<html lang="en">
<head>
<meta charset="utf-8">
<title>Tolliver for Governor — Stationery</title>
<link href="https://fonts.googleapis.com/css2?family=Tinos:wght@400;700&family=Arimo:wght@400;700&display=swap" rel="stylesheet">
<style>
:root{
  --stage:#2e2f31;
  --paper:#ffffff;
  --blue:#1665bd;
  --blue-deep:#0b4a93;
  --blue-light:#3f8fe0;
  --ring:#1c6fc8;
  --ink:#333a44;
  --muted:#8a96a6;
  --wash:#e4edf6;
}
*{margin:0;padding:0;box-sizing:border-box}
html,body{width:1200px;height:828px;overflow:hidden;background:var(--stage)}
.canvas{position:relative;width:1200px;height:828px;font-family:"Arimo",Arial,sans-serif;color:var(--ink)}
.piece{position:absolute;overflow:hidden;background:var(--paper)}
.serif{font-family:"Tinos","Times New Roman",serif}

/* logo lockup: plain circle + name */
.mark{position:absolute;border-radius:50%;background:var(--paper);border:3px solid var(--ring)}
.name{position:absolute;font-family:"Tinos","Times New Roman",serif;font-weight:700;color:var(--blue);line-height:1;white-space:nowrap}
.name.white{color:#fff}

.blue-field{background:radial-gradient(ellipse at 50% 45%,var(--blue-light) 0%,var(--blue) 45%,var(--blue-deep) 100%)}
.band{position:absolute;background:linear-gradient(90deg,var(--blue-deep),var(--blue) 60%,var(--blue-light))}

/* business cards */
.card{width:137px;height:77px;border-radius:5px}
.card .tiny{position:absolute;font-size:5px;line-height:1.35;color:var(--ink);white-space:nowrap}
.card .person{position:absolute;font-size:6px;font-weight:700;color:#fff;white-space:nowrap}
.slogan-card{position:absolute;font-family:"Tinos",serif;font-weight:700;color:#fff;white-space:nowrap}

/* letterhead */
.letterhead{left:336px;top:202px;width:350px;height:441px}
.letterhead .watermark-ring{position:absolute;left:105px;top:160px;width:140px;height:140px;border-radius:50%;border:10px solid var(--wash)}
.letterhead .watermark-text{position:absolute;left:0;right:0;top:305px;text-align:center;font-family:"Tinos",serif;font-weight:700;font-size:17px;color:#dfe5ec}
.foot{position:absolute;font-size:5px;line-height:1.4;color:var(--ink);white-space:nowrap}

/* envelope */
.env-back{width:408px;height:173px}
.env-slogan{position:absolute;left:0;right:0;text-align:center;font-family:"Tinos",serif;font-weight:700;color:#fff;font-size:26px}
.env-front{left:720px;top:473px;width:454px;height:170px}
</style>
</head>
<body>
<div class="canvas">

  <!-- Business cards: row 1 -->
  <div class="piece card" style="left:29px;top:274px">
    <div class="band" style="left:0;right:0;top:12px;height:12px"></div>
    <div class="mark" style="left:10px;top:6px;width:26px;height:26px"></div>
    <div class="person" style="left:44px;top:14px">Jorel Drennick</div>
    <div class="name" style="left:7px;top:35px;font-size:11px">Tolliver</div>
    <div class="tiny" style="left:60px;top:34px">Campaign Manager<br>(317) 555-0148<br>P.O. Box 71832<br>Indianapolis, IN 46917</div>
  </div>
  <div class="piece card" style="left:173px;top:274px">
    <div class="band" style="left:0;right:0;top:12px;height:12px"></div>
    <div class="mark" style="left:55px;top:6px;width:26px;height:26px"></div>
    <div class="name" style="left:44px;top:35px;font-size:11px">Tolliver</div>
    <div class="tiny" style="left:30px;top:52px;color:var(--blue)">www.TolliverForGovernor.example</div>
  </div>

  <!-- row 2 -->
  <div class="piece card blue-field" style="left:29px;top:360px">
    <div class="mark" style="left:20px;top:12px;width:52px;height:52px"></div>
  </div>
  <div class="piece card blue-field" style="left:173px;top:360px">
    <div class="mark" style="left:52px;top:8px;width:32px;height:32px"></div>
    <div class="name white" style="left:40px;top:46px;font-size:14px">Tolliver</div>
  </div>

  <!-- row 3 -->
  <div class="piece card" style="left:29px;top:446px">
    <div class="band" style="left:32px;right:0;top:0;bottom:0"></div>
    <div class="mark" style="left:4px;top:6px;width:24px;height:24px"></div>
    <div class="name" style="left:-6px;top:48px;font-size:10px;transform:rotate(-90deg)">Tolliver</div>
    <div class="person" style="left:44px;top:10px">Jorel Drennick</div>
  </div>
  <div class="piece card blue-field" style="left:173px;top:446px">
    <div class="slogan-card" style="left:10px;top:18px;font-size:10px">It's Our Time</div>
    <div class="mark" style="left:94px;top:10px;width:28px;height:28px"></div>
    <div class="name white" style="left:78px;top:50px;font-size:14px">Tolliver</div>
  </div>

  <!-- Letterhead -->
  <div class="piece letterhead">
    <div class="band" style="left:30px;right:0;top:20px;height:16px"></div>
    <div class="serif" style="position:absolute;right:14px;top:22px;font-size:9px;font-weight:700;color:#fff">It's Our Time</div>
    <div class="mark" style="left:28px;top:10px;width:36px;height:36px"></div>
    <div class="name" style="left:18px;top:50px;font-size:16px">Tolliver</div>
    <div class="watermark-ring"></div>
    <div class="watermark-text">It's Our Time</div>
    <div class="foot" style="left:14px;bottom:12px">Paid For By Tolliver For Governor</div>
    <div class="foot" style="right:16px;bottom:12px;text-align:right">P.O. Box 71832<br>Indianapolis, IN 46917<br>(317) 555-0148<br>www.TolliverForGovernor.example</div>
    <div style="position:absolute;right:0;bottom:10px;width:4px;height:26px;background:var(--blue)"></div>
  </div>

  <!-- Envelope back, panel and flap -->
  <div class="piece env-back blue-field" style="left:763px;top:96px">
    <div class="env-slogan" style="top:98px">It's Our Time</div>
  </div>
  <div class="piece env-back blue-field" style="left:763px;top:288px">
    <div class="mark" style="left:180px;top:20px;width:48px;height:48px"></div>
    <div class="env-slogan" style="top:110px">It's Our Time</div>
  </div>

  <!-- Envelope front -->
  <div class="piece env-front">
    <div class="band" style="left:40px;right:0;top:14px;height:16px"></div>
    <div class="serif" style="position:absolute;right:14px;top:16px;font-size:9px;font-weight:700;color:#fff">It's Our Time</div>
    <div class="mark" style="left:30px;top:6px;width:34px;height:34px"></div>
    <div class="name" style="left:20px;top:43px;font-size:15px">Tolliver</div>
    <div class="foot" style="left:20px;top:60px">P.O. Box 71832 · Indianapolis, IN 46917</div>
    <div style="position:absolute;left:245px;top:70px;width:80px;height:80px;border-radius:50%;border:7px solid var(--wash)"></div>
  </div>

</div>
</body>
</html>
```